Business Card Project for Firm Deck Hoisting

Business name is "Firm Deck Hoisting" we are a scaffolding & rigging business specialising in local and remote work for:
- scaffolding (residential, commercial, industrial)
- rigging
-man material hoists
- swing stages
- labour hire

On the back of the card I would like FDH as the symbol / logo. I have attached the logos we have had created by sketch harbour. We would like to use bold colours – preferably as the same colour scheme as the logo.

Target Market(s)

Construction business

Industry/Entity Type

Construction

Contact Information for Business Card

name: Owen Pellew
Title: Director
Phone: 0491 572 864
Address: PO BOX 3251, Kellbrook SA 5921
Email: owen@firmdeckhoisting.com.au
Website: www.firmdeckhoisting.com.au

Font styles to use
Sans Serif

Requirements
Must have
• Must use existing logo & prefering using bold colours
Nice to have
• Would be nice to have a line of dot points in what we specialise in but not essential
• Would be nice to see some designs with a slogan but not essential
Should not have
• NA

```html
<!DOCTYPE html>
<html lang="en">
<head>
<meta charset="utf-8">
<title>Firm Deck Hoisting — Business Card</title>
<link rel="stylesheet" href="https://fonts.googleapis.com/css2?family=Roboto:wght@400;500;700&display=swap">
<style>
  :root {
    --backdrop: #2b2421;
    --card: #0e0e10;
    --white: #f4f4f4;
    --blue: #2f80d1;
    --muted: #d9d9d9;
  }
  * { margin: 0; padding: 0; box-sizing: border-box; }
  html, body {
    width: 1200px;
    height: 829px;
    overflow: hidden;
    background: var(--backdrop);
    font-family: "Roboto", Arial, sans-serif;
  }
  .canvas {
    width: 1200px;
    height: 829px;
    display: flex;
    align-items: center;
    justify-content: center;
    gap: 40px;
  }
  .card {
    width: 540px;
    height: 300px;
    background: var(--card);
    border-radius: 4px;
    box-shadow: 0 10px 30px rgba(0,0,0,.45);
    position: relative;
    color: var(--white);
  }
  .wordmark {
    display: flex;
    align-items: center;
    gap: 12px;
  }
  .wordmark-square {
    width: 18px;
    height: 18px;
    background: var(--blue);
  }
  .wordmark-name {
    font-weight: 700;
    font-size: 26px;
    letter-spacing: 1px;
    text-transform: uppercase;
    color: var(--white);
  }

  /* front */
  .card-front .wordmark {
    position: absolute;
    left: 60px;
    top: 62px;
  }
  .contact-block {
    position: absolute;
    left: 60px;
    top: 140px;
    display: flex;
    gap: 22px;
  }
  .person {
    text-align: right;
    padding-top: 26px;
  }
  .person-name {
    font-weight: 500;
    font-size: 15px;
    letter-spacing: .3px;
  }
  .person-title {
    font-size: 13px;
    color: var(--blue);
    margin-top: 3px;
    letter-spacing: .5px;
  }
  .contact-list {
    list-style: none;
    font-size: 13px;
    line-height: 19px;
    color: var(--muted);
  }
  .contact-list li {
    display: flex;
    align-items: center;
    gap: 8px;
  }
  .contact-icon {
    width: 12px;
    height: 12px;
    flex: none;
  }
  .website {
    position: absolute;
    left: 0;
    right: 0;
    bottom: 40px;
    text-align: center;
    font-size: 13px;
    color: var(--muted);
    letter-spacing: .3px;
  }

  /* back */
  .card-back {
    display: flex;
    flex-direction: column;
    align-items: center;
  }
  .card-back .wordmark { margin-top: 92px; }
  .services {
    margin-top: 70px;
    text-align: center;
    font-size: 10.5px;
    line-height: 17px;
    letter-spacing: .4px;
    text-transform: uppercase;
    color: var(--white);
  }
  .service-dot {
    display: inline-block;
    width: 6px;
    height: 6px;
    border-radius: 50%;
    background: var(--blue);
    margin: 0 6px;
    vertical-align: 1px;
  }
</style>
</head>
<body>
<main class="canvas">

  <section class="card card-front" aria-label="Card front">
    <div class="wordmark">
      <span class="wordmark-square"></span>
      <span class="wordmark-name">Firm Deck Hoisting</span>
    </div>

    <div class="contact-block">
      <div class="person">
        <p class="person-name">OWEN PELLEW</p>
        <p class="person-title">DIRECTOR</p>
      </div>
      <ul class="contact-list">
        <li>
          <svg class="contact-icon" viewBox="0 0 12 12" aria-hidden="true">
            <rect width="12" height="12" rx="2" fill="var(--blue)"/>
            <path d="M6 2.2a2.6 2.6 0 0 0-2.6 2.6C3.4 7 6 9.8 6 9.8S8.6 7 8.6 4.8A2.6 2.6 0 0 0 6 2.2z" fill="#fff"/>
            <circle cx="6" cy="4.8" r="1" fill="var(--blue)"/>
          </svg>
          PO BOX 3251, Kellbrook SA 5921
        </li>
        <li>
          <svg class="contact-icon" viewBox="0 0 12 12" aria-hidden="true">
            <rect width="12" height="12" rx="2" fill="var(--blue)"/>
            <path d="M3.6 2.6l1.3-.2.8 1.9-.9.7a5 5 0 0 0 2.2 2.2l.7-.9 1.9.8-.2 1.3c-3.4.4-6.2-2.4-5.8-5.8z" fill="#fff"/>
          </svg>
          0491 572 864
        </li>
        <li>
          <svg class="contact-icon" viewBox="0 0 12 12" aria-hidden="true">
            <rect width="12" height="12" rx="2" fill="var(--blue)"/>
            <rect x="2.4" y="3.4" width="7.2" height="5.2" fill="#fff"/>
            <path d="M2.4 3.4L6 6.4l3.6-3" stroke="var(--blue)" stroke-width=".9" fill="none"/>
          </svg>
          owen@firmdeckhoisting.com.au
        </li>
      </ul>
    </div>

    <p class="website">www.firmdeckhoisting.com.au</p>
  </section>

  <section class="card card-back" aria-label="Card back">
    <div class="wordmark">
      <span class="wordmark-square"></span>
      <span class="wordmark-name">Firm Deck Hoisting</span>
    </div>
    <div class="services">
      <p>Scaffolding (Residential, Commercial, Industrial)</p>
      <p>Rigging<span class="service-dot"></span>Man Material Hoists<span class="service-dot"></span>Swing Stages<span class="service-dot"></span>Labour Hire</p>
    </div>
  </section>

</main>
</body>
</html>
```